Business card design needed

Family General Practitioner/ Family Physician.
Logo is the logo of the Crestmoor Guild of Family Clinicians Australia
http://kvplm.tarevo.edu.au/PictureGallery/logos/pages/CGFC%20logo_jpg.htm

Reason: Just a bit more time to make changes and the weekend for me to look at things closely and to choose. Thanks, Lumi

Thanks for all the submissions. So many of them are really works of art. Not one of them are not good. The ones that I am eliminating are the ones that I think are not suitable for me personally only, and because if I don't, it makes it very difficult to decide as many of you are also sending me slight variations of a card. I have just decided to choose a second place card too. Can't thank you all enough. Good luck, Lumi. P.S - Working today till 10 pm as the card says :-), so probably won't be able to give a feedback till late Saturday night or Sunday morning here in Sydney, Australia. 

Reason: Just added a second place to the budget and realised that Australia is ahead of the rest of the world in the time zone (only :-) - don't want to offend anyone or start a debate!! ) , so Monday deadline will mean it will be a weekend for the rest of the world. Just wanted to give everyone more time to submit their best, especially since I will be picking a second card too. Can't thank everyone enough for the submissions. P.S - Not keen on photos on the card.

Contact Information for Business Card

Dr. Lumi Harcourt M.B.B.S., F.C.G.F.C
Family General Practitioner
Address, timings, phone and fax number on the back.

Requirements
Must have
• Timings
Mon 7 am - 7 pm
Tues 7 am - 12 pm
Wed 7 am - 10 pm
Thurs 7 am - 12 pm
Fri 7 am - 8 pm
Sat 8 am - 10 pm
Sun - Off

```html
<!DOCTYPE html>
<html lang="en">
<head>
<meta charset="utf-8">
<title>Dr. Lumi Harcourt – Business Card</title>
<link rel="stylesheet" href="https://fonts.googleapis.com/css2?family=Source+Sans+3:ital,wght@0,400;0,700;1,400&display=swap">
<style>
  :root {
    --page-bg: #d9d9d9;
    --card-bg: #ffffff;
    --band: #59595b;
    --ink-dark: #4a4a4c;
    --ink-mid: #6a6a6c;
    --ink-light: #9b9b9d;
    --on-band: #ffffff;
    --crest-red: #c8262c;
  }
  * { box-sizing: border-box; margin: 0; padding: 0; }
  html, body {
    width: 1200px; height: 848px; overflow: hidden;
    background: var(--page-bg);
    font-family: "Source Sans 3", "Myriad Pro", Arial, sans-serif;
  }
  .canvas { position: relative; width: 1200px; height: 848px; }

  .card {
    position: absolute;
    width: 580px; height: 332px;
    background: var(--card-bg);
    overflow: hidden;
    box-shadow: 0 6px 18px rgba(0,0,0,0.22);
  }
  .card--front { left: 70px; top: 70px; }
  .card--back  { left: 550px; top: 446px; }

  .band {
    position: absolute; left: 0; right: 0; bottom: 0;
    background: var(--band);
  }

  /* Front */
  .brand {
    position: absolute; left: 58px; top: 104px;
    display: flex; align-items: center; gap: 10px;
  }
  .brand__mark { width: 22px; height: 22px; border-radius: 50%; background: var(--crest-red); }
  .brand__name {
    font-size: 30px; font-weight: 700; color: var(--crest-red); letter-spacing: 1px;
  }
  .identity {
    position: absolute; left: 236px; top: 82px; text-align: center; width: 300px;
  }
  .identity__name { font-size: 29px; font-weight: 700; color: var(--ink-dark); line-height: 1.1; }
  .identity__credentials,
  .identity__role { font-size: 17px; color: var(--ink-mid); line-height: 1.3; }
  .identity__credentials { margin-top: 10px; }
  .identity__role { font-style: italic; }
  .card--front .band { height: 72px; display: flex; align-items: center; justify-content: center; }
  .tagline { font-size: 27px; font-style: italic; color: var(--on-band); }

  /* Back */
  .hours {
    position: absolute; left: 0; right: 0; top: 30px; text-align: center;
    font-size: 24px; font-weight: 700; color: var(--ink-dark); line-height: 1.5;
  }
  .address {
    position: absolute; left: 0; right: 0; top: 160px; text-align: center;
    font-size: 17px; font-style: italic; color: var(--ink-light); line-height: 1.3;
  }
  .contact {
    position: absolute; left: 0; right: 0; top: 214px; text-align: center;
    font-size: 20px; color: var(--ink-light);
  }
  .contact__phone { font-weight: 700; }
  .card--back .band { height: 62px; }
</style>
</head>
<body>
<main class="canvas">

  <section class="card card--front" aria-label="Business card front">
    <div class="brand">
      <span class="brand__mark"></span>
      <span class="brand__name">CGFC</span>
    </div>
    <div class="identity">
      <h1 class="identity__name">Dr. Lumi Harcourt</h1>
      <p class="identity__credentials">M.B.B.S., F.C.G.F.C</p>
      <p class="identity__role">Family General Practitioner</p>
    </div>
    <div class="band">
      <p class="tagline">"Caring about your health"</p>
    </div>
  </section>

  <section class="card card--back" aria-label="Business card back">
    <div class="hours">
      <p>Mon 7am - 7pm • Tues 7am - 12pm</p>
      <p>Wed 7am - 10pm • Thurs 7am - 12pm</p>
      <p>Fri 7am - 8pm • Sat 8am - 10pm</p>
    </div>
    <address class="address">
      Upper Level, Garden Court, Elmridge Shopping Centre<br>
      Elmridge, NSW 2199
    </address>
    <p class="contact">
      <span class="contact__phone">P: 02 5550 1400</span> • F: 02 5550 1233
    </p>
    <div class="band"></div>
  </section>

</main>
</body>
</html>
```